Building company buisness cards

We are looking for a sharp modern new look for our business cards.
We are a New Zealand based company that specialises in house and land packages.
We have attached a photo of the current logo and would like to see if it can be improved somehow if needed.
We are open to any colours but we have chosen green at this stage.
Feel free to change the font and make the logo smarter looking.
Play with the colours and see what looks best.

We want a card that looks so good know one will want to throw it away!

Target Market(s)

Home buyers

Industry/Entity Type

Building

Contact Information for Business Card

Dorian Keswick
0217392604
dkeswick@tidewellhomecraft.co.nz
tidewellhomecraft.co.nz

Font styles to use
Serif
Sans Serif

Colors

Designer to choose colors to be used in the design.

Requirements
Must have
• Logo and company name on one side, details on the other side
Nice to have
• Color codes for the original green are HEX #4a8028, RGB(74,128,40), CMYK(42,0,69,50)
• Round corners, Raised and/or spot UV

```html
<!DOCTYPE html>
<html lang="en">
<head>
<meta charset="utf-8">
<title>Tidewell Homecraft — Business Card</title>
<link rel="stylesheet" href="https://fonts.googleapis.com/css2?family=Cinzel:wght@600&family=Jost:wght@400;600&display=swap">
<style>
  :root {
    --backdrop: #2b2b2b;
    --card-white: #ffffff;
    --brand-green: #4a8028;
    --text-grey: #4d4d4d;
    --on-green: #ffffff;
  }
  * { margin: 0; padding: 0; box-sizing: border-box; }
  html, body {
    width: 1125px;
    height: 1200px;
    overflow: hidden;
    background: var(--backdrop);
  }
  .canvas {
    position: relative;
    width: 1125px;
    height: 1200px;
  }
  .card {
    position: absolute;
    left: 150px;
    width: 825px;
    height: 472px;
    border-radius: 26px;
    display: flex;
    flex-direction: column;
    align-items: center;
  }
  .card--details {
    top: 98px;
    background: var(--card-white);
  }
  .card--brand {
    top: 631px;
    background: var(--brand-green);
    justify-content: center;
  }
  .brand-mark {
    display: flex;
    align-items: center;
    gap: 14px;
    font-family: "Jost", sans-serif;
    font-weight: 600;
    text-transform: uppercase;
  }
  .brand-mark__square {
    display: block;
    background: currentColor;
  }
  .card--details .brand-mark {
    margin-top: 176px;
    color: var(--brand-green);
    font-size: 26px;
    letter-spacing: 3px;
  }
  .card--details .brand-mark__square { width: 18px; height: 18px; }
  .holder-name {
    margin-top: 22px;
    font-family: "Cinzel", serif;
    font-weight: 600;
    font-size: 33px;
    letter-spacing: 1.5px;
    color: var(--brand-green);
  }
  .contact {
    margin-top: 18px;
    list-style: none;
    text-align: center;
    font-family: "Jost", sans-serif;
    font-weight: 400;
    font-size: 19.5px;
    line-height: 26px;
    color: var(--text-grey);
  }
  .card--brand .brand-mark {
    color: var(--on-green);
    font-size: 46px;
    letter-spacing: 2px;
    gap: 20px;
  }
  .card--brand .brand-mark__square { width: 30px; height: 30px; }
</style>
</head>
<body>
  <main class="canvas">
    <section class="card card--details" aria-label="Business card, contact side">
      <div class="brand-mark">
        <span class="brand-mark__square" aria-hidden="true"></span>
        <span class="brand-mark__name">Tidewell Homecraft</span>
      </div>
      <h1 class="holder-name">DORIAN KESWICK</h1>
      <ul class="contact">
        <li class="contact__phone">P. 0217392604</li>
        <li class="contact__email">dkeswick@tidewellhomecraft.co.nz</li>
        <li class="contact__web">tidewellhomecraft.co.nz</li>
      </ul>
    </section>

    <section class="card card--brand" aria-label="Business card, brand side">
      <div class="brand-mark">
        <span class="brand-mark__square" aria-hidden="true"></span>
        <span class="brand-mark__name">Tidewell Homecraft</span>
      </div>
    </section>
  </main>
</body>
</html>
```